Design a For Sale sign board and Direction Sign Board.
Attached is an example of what i am thinking but am happy to look at any options.
Colours are to be ""bright Orange"on white and in reverse as well.

Logo Text

Logo id Brookvale & Co Real Estate.

```html
<!DOCTYPE html>
<html lang="en">
<head>
<meta charset="utf-8">
<title>Brookvale &amp; Co Real Estate – Sign Boards</title>
<link href="https://fonts.googleapis.com/css2?family=Montserrat:wght@600;700;800&display=swap" rel="stylesheet">
<style>
  :root {
    --orange: #e5501f;
    --white: #ffffff;
    --black: #111111;
    --page: #eeeeee;
  }
  * { box-sizing: border-box; margin: 0; padding: 0; }
  html, body { width: 986px; height: 1200px; overflow: hidden; }
  body {
    background: var(--page);
    font-family: "Montserrat", Arial, sans-serif;
    display: flex;
    flex-direction: column;
    align-items: center;
    justify-content: space-evenly;
  }
  .sign {
    width: 560px;
    height: 545px;
    background: var(--white);
    display: flex;
    flex-direction: column;
    box-shadow: 0 4px 14px rgba(0,0,0,0.15);
  }
  .sign__brand {
    height: 285px;
    background: var(--orange);
    color: var(--white);
    display: flex;
    flex-direction: column;
    align-items: center;
    justify-content: center;
    font-weight: 700;
    text-align: center;
  }
  .brand-name { font-size: 50px; letter-spacing: 0.5px; line-height: 1.1; }
  .brand-tagline { font-size: 26px; letter-spacing: 1px; margin-top: 10px; }
  .sign__agent {
    flex: 1;
    display: flex;
    flex-direction: column;
    align-items: center;
    padding-top: 26px;
  }
  .agent-name {
    color: var(--orange);
    font-weight: 700;
    font-size: 60px;
    line-height: 1;
    letter-spacing: 0.5px;
  }
  .agent-phone {
    display: flex;
    align-items: center;
    gap: 14px;
    margin-top: 22px;
    color: var(--black);
    font-weight: 800;
    font-size: 44px;
  }
  .phone-banner {
    position: relative;
    width: 500px;
    height: 62px;
    margin-top: 22px;
  }
  .phone-banner svg { position: absolute; inset: 0; }
  .phone-banner__number {
    position: absolute;
    left: 70px;
    top: 0;
    height: 62px;
    display: flex;
    align-items: center;
    color: var(--orange);
    font-weight: 800;
    font-size: 32px;
  }
  .sign__base {
    margin-top: auto;
    display: flex;
    flex-direction: column;
  }
  .base-stripe--orange { height: 12px; background: var(--orange); }
  .base-gap { height: 5px; background: var(--white); }
  .base-stripe--black { height: 12px; background: var(--black); }
</style>
</head>
<body>

  <section class="sign sign--speed">
    <div class="sign__brand">
      <p class="brand-name">BROOKVALE &amp; CO.</p>
      <p class="brand-tagline">REAL ESTATE</p>
    </div>
    <div class="sign__agent">
      <p class="agent-name">DANIEL HARPER</p>
      <p class="agent-phone">
        <svg width="56" height="30" viewBox="0 0 56 30" aria-hidden="true">
          <rect x="0" y="4" width="56" height="4" fill="#111"/>
          <rect x="14" y="13" width="42" height="4" fill="#111"/>
          <rect x="28" y="22" width="28" height="4" fill="#111"/>
        </svg>
        <span>0400 123 678</span>
        <svg width="56" height="30" viewBox="0 0 56 30" aria-hidden="true">
          <rect x="0" y="4" width="56" height="4" fill="#111"/>
          <rect x="0" y="13" width="42" height="4" fill="#111"/>
          <rect x="0" y="22" width="28" height="4" fill="#111"/>
        </svg>
      </p>
    </div>
    <div class="sign__base">
      <div class="base-stripe--orange"></div>
      <div class="base-gap"></div>
      <div class="base-stripe--black"></div>
    </div>
  </section>

  <section class="sign sign--arrow">
    <div class="sign__brand">
      <p class="brand-name">BROOKVALE &amp; CO.</p>
      <p class="brand-tagline">REAL ESTATE</p>
    </div>
    <div class="sign__agent">
      <p class="agent-name">DANIEL HARPER</p>
      <div class="phone-banner">
        <svg width="500" height="62" viewBox="0 0 500 62" aria-hidden="true">
          <polygon points="32,0 500,0 470,31 500,62 32,62 0,31" fill="#111"/>
          <polyline points="400,12 418,31 400,50" fill="none" stroke="#fff" stroke-width="6"/>
          <polyline points="420,12 438,31 420,50" fill="none" stroke="#fff" stroke-width="6"/>
          <polyline points="440,12 458,31 440,50" fill="none" stroke="#fff" stroke-width="6"/>
        </svg>
        <span class="phone-banner__number">0400 123 678</span>
      </div>
    </div>
    <div class="sign__base">
      <div class="base-stripe--orange"></div>
      <div class="base-gap"></div>
      <div class="base-stripe--black"></div>
    </div>
  </section>

</body>
</html>
```